Cradle Glow Events

New Company ,I will attened clients personal residents(venu of there choice) and provide 3D ultra sound photos at time of ultra sound.This is a Non diagnostic ultra sound which does not replace the ultrasound reqested by Dr.The best time for ultra sound is 24 to 34 weeks.The baby sex can be kept confidential if requied and all cultral and diverse backgrounds cattered for..No referal requied for this.I have 2 main packges,1 baby shower and 2 family time.Extra options available are entertainment,Family time prior to baby shower for dad,decoration, Kids entertainment.
Contact number is 0471938402 email to be added ASAP.
prices start from $450

It Company

```html
<!DOCTYPE html>
<html lang="en">
<head>
<meta charset="utf-8">
<title>Cradle Glow Events</title>
<link href="https://fonts.googleapis.com/css2?family=Open+Sans:wght@400;600;700;800&display=swap" rel="stylesheet">
<style>
  :root {
    --magenta: #d81b5f;
    --plum: #9c1c5f;
    --orange: #f15a24;
    --frame: #9a2061;
    --paper: #f1f1f1;
    --white: #ffffff;
  }
  html, body {
    margin: 0;
    padding: 0;
    overflow: hidden;
    background: var(--white);
  }
  .flyer {
    position: relative;
    width: 928px;
    height: 1200px;
    box-sizing: border-box;
    border: 8px solid var(--frame);
    background: radial-gradient(ellipse at 50% 40%, #ffffff 0%, #f4f4f4 55%, #e6e6e6 100%);
    font-family: "Open Sans", Arial, sans-serif;
    overflow: hidden;
  }
  .hero {
    position: absolute;
    left: 0;
    top: 0;
    width: 912px;
    height: 380px;
  }
  .brand {
    position: absolute;
    left: 0;
    right: 0;
    top: 440px;
    display: flex;
    align-items: center;
    justify-content: center;
    gap: 20px;
  }
  .brand-dot {
    width: 46px;
    height: 46px;
    border-radius: 50%;
    background: var(--magenta);
  }
  .brand-name {
    margin: 0;
    font-size: 62px;
    font-weight: 700;
    color: var(--magenta);
    letter-spacing: -0.5px;
  }
  .features {
    position: absolute;
    left: 29px;
    top: 627px;
    width: 854px;
    margin: 0;
    padding: 0;
    list-style: none;
  }
  .feature {
    display: flex;
    align-items: center;
    justify-content: center;
    text-align: center;
    color: var(--white);
    font-weight: 700;
    font-size: 22px;
    line-height: 31px;
    text-transform: uppercase;
    padding: 0 20px;
    box-sizing: border-box;
  }
  .feature--tall { height: 74px; }
  .feature--short { height: 42px; }
  .feature--magenta { background: var(--magenta); }
  .feature--plum { background: var(--plum); }
  .feature--orange { background: var(--orange); }
  .price {
    position: absolute;
    left: 29px;
    top: 934px;
    width: 251px;
    height: 206px;
    background: var(--orange);
    color: var(--white);
    text-align: center;
    box-sizing: border-box;
    padding-top: 20px;
  }
  .price-label {
    margin: 0 auto;
    width: 210px;
    font-size: 22px;
    line-height: 28px;
    font-weight: 400;
    text-transform: uppercase;
    padding-bottom: 8px;
    border-bottom: 2px solid var(--white);
  }
  .price-amount {
    margin: 0 auto;
    width: 210px;
    font-size: 72px;
    line-height: 96px;
    font-weight: 700;
    border-bottom: 2px solid var(--white);
  }
  .contact {
    position: absolute;
    left: 308px;
    top: 930px;
    width: 577px;
  }
  .contact-heading {
    margin: 0;
    font-size: 26px;
    font-weight: 700;
    color: var(--plum);
    text-transform: uppercase;
    letter-spacing: 0.3px;
    padding-bottom: 8px;
    border-bottom: 3px solid var(--orange);
  }
  .phone {
    margin-top: 20px;
    height: 103px;
    background: var(--magenta);
    display: flex;
    align-items: center;
    padding-left: 14px;
    gap: 14px;
    color: var(--white);
    font-size: 64px;
    font-weight: 700;
    letter-spacing: 0.5px;
  }
  .phone-icon {
    width: 68px;
    height: 68px;
    flex: none;
  }
</style>
</head>
<body>
<main class="flyer">
  <svg class="hero" viewBox="0 0 912 380" aria-hidden="false">
    <defs>
      <linearGradient id="heroTone" x1="0" y1="0" x2="1" y2="1">
        <stop offset="0" stop-color="#6b5a5e"/>
        <stop offset="0.35" stop-color="#c9a49a"/>
        <stop offset="0.6" stop-color="#e2c3b8"/>
        <stop offset="1" stop-color="#7f7e8c"/>
      </linearGradient>
      <clipPath id="heroClip">
        <path d="M0 0 H912 V332 C800 300 690 262 560 258 C420 254 330 300 220 302 C130 304 60 282 0 268 Z"/>
      </clipPath>
    </defs>
    <g role="img" aria-label="Photo of an expectant mother holding a 3D ultrasound print in front of her belly">
      <rect x="0" y="0" width="912" height="380" fill="url(#heroTone)" clip-path="url(#heroClip)"/>
    </g>
    <path d="M0 268 C60 282 130 304 220 302 C330 300 420 254 560 258 C690 262 800 300 912 332 V352 C790 318 680 290 560 288 C430 286 330 330 220 332 C120 334 55 308 0 296 Z" fill="var(--magenta)"/>
  </svg>

  <header class="brand">
    <span class="brand-dot"></span>
    <h1 class="brand-name">Cradle Glow Events</h1>
  </header>

  <ul class="features">
    <li class="feature feature--tall feature--magenta">3D ultrasounds in the comfort of your own home or a venue of your choice!</li>
    <li class="feature feature--short feature--plum">All cultures cattered for!</li>
    <li class="feature feature--tall feature--orange">Non-diagnostic – doesn’t replace ultrasound requested by your doctor!</li>
    <li class="feature feature--short feature--magenta">No refferal required!</li>
    <li class="feature feature--short feature--plum">Sex of baby can be kept confidential!</li>
  </ul>

  <section class="price">
    <p class="price-label">Prices start from only</p>
    <p class="price-amount">$450</p>
  </section>

  <section class="contact">
    <h2 class="contact-heading">Call now for more information:</h2>
    <div class="phone">
      <svg class="phone-icon" viewBox="0 0 68 68" aria-hidden="true">
        <circle cx="34" cy="34" r="31" fill="none" stroke="#ffffff" stroke-width="4"/>
        <path d="M26 16 C22 17 19 21 19 26 C20 38 30 48 42 49 C47 49 51 46 52 42 L45 36 C43 35 41 36 40 38 C35 37 31 33 30 28 C32 27 33 25 32 23 Z" fill="#ffffff"/>
      </svg>
      <span class="phone-number">0471938402</span>
    </div>
  </section>
</main>
</body>
</html>
```